First Birthday Party Invitation

We need a flyer/invitation design for our baby girl Marisol's first birthday party. We want the design to look like a club event flyer. The party will have a sailing/nautical theme and will be at a marina but in Miami so the invite must have a cool, non-baby, non-kitchy vibe.

Here's the text...feel free to play around with it!

Welcome Aboard! 

We'll have lots of fun

Our little Marisol is turning one!

You're invited to a party

on Saturday, August 7th from 5 - 7 p.m.

Tide-And-Rope Miami

Third Floor
4187 North Coralwind Avenue
Miami, FL 33149-7812
Parking tickets will be validated 

Please RSVP by July 31st to MarisolBirthday@bluefinmail.test or 305.482.9067

Arrive early at 4 p.m. to join us on a short pre-party boat tour of the Miami skyline

Flyer should be one-sided only.  It will be printed in color and also emailed. 

Important update - please add small text that says "No gifts please.  A contribution to Tide And Rope's programs would be greatly appreciated."

```html
<!DOCTYPE html>
<html lang="en">
<head>
<meta charset="utf-8">
<title>Marisol's Birthday</title>
<link rel="stylesheet" href="https://fonts.googleapis.com/css2?family=Cinzel:wght@700;900&family=Marcellus+SC&display=swap">
<style>
  :root {
    --ink: #000000;
    --rose: #c97a7c;
    --rose-deep: #7a3d40;
    --paper: #f3eeec;
    --bubble: #3a3a3a;
  }
  * { margin: 0; padding: 0; box-sizing: border-box; }
  html, body { width: 991px; height: 1200px; overflow: hidden; background: var(--ink); }
  .flyer {
    position: relative;
    width: 991px;
    height: 1200px;
    background: var(--ink);
    color: var(--paper);
    font-family: "Marcellus SC", "Cinzel", serif;
    overflow: hidden;
  }
  .headline {
    position: absolute;
    left: 0;
    width: 991px;
    text-align: center;
    font-family: "Cinzel", serif;
    font-weight: 900;
    color: var(--rose);
    white-space: nowrap;
    line-height: 1;
  }
  .headline--name { top: 6px; font-size: 128px; letter-spacing: 2px; padding-left: 10px; }
  .headline--reflection {
    top: 122px;
    font-size: 128px;
    letter-spacing: 2px;
    padding-left: 10px;
    transform: scaleY(-0.7);
    transform-origin: top;
    opacity: 0.35;
    -webkit-mask-image: linear-gradient(to top, rgba(0,0,0,0.9), transparent 70%);
            mask-image: linear-gradient(to top, rgba(0,0,0,0.9), transparent 70%);
    color: var(--rose-deep);
  }
  .headline--occasion { top: 1010px; font-size: 126px; letter-spacing: 4px; padding-left: 20px; }

  .compass-art { position: absolute; left: 40px; top: 270px; }

  .bubbles { position: absolute; left: 0; top: 0; pointer-events: none; }

  .details { position: absolute; left: 517px; white-space: nowrap; line-height: 1.12; }
  .details p { display: block; }
  .welcome { top: 226px; }
  .welcome .lead { font-size: 29px; letter-spacing: 2px; }
  .welcome .sub { font-size: 22px; letter-spacing: 0.5px; }
  .party { top: 410px; }
  .party .lead { font-size: 28px; }
  .party .sub { font-size: 19px; margin-top: 4px; }
  .party .venue { font-size: 25px; letter-spacing: 1px; margin-top: 4px; }
  .address { top: 584px; }
  .address .floor { font-family: "Cinzel", serif; font-weight: 700; font-size: 33px; letter-spacing: 3px; }
  .address .line { font-size: 22px; margin-top: 4px; }
  .address .city { font-size: 24px; margin-top: 2px; }
  .address .note { font-size: 17px; letter-spacing: 0.5px; margin-top: 4px; }

  .footnote { position: absolute; left: 0; width: 991px; text-align: center; white-space: nowrap; }
  .rsvp { top: 800px; font-size: 22px; }
  .early { top: 838px; font-size: 18px; }
  .gifts { top: 928px; font-size: 16px; }
</style>
</head>
<body>
<main class="flyer">
  <h1 class="headline headline--name">MARISOL'S</h1>
  <div class="headline headline--reflection" aria-hidden="true">MARISOL'S</div>

  <svg class="bubbles" width="991" height="1200" aria-hidden="true">
    <g fill="var(--bubble)" opacity="0.8">
      <circle cx="604" cy="545" r="11"/>
      <circle cx="550" cy="565" r="10"/>
      <circle cx="506" cy="568" r="7"/>
      <circle cx="603" cy="760" r="16"/>
      <circle cx="588" cy="742" r="10"/>
      <circle cx="610" cy="780" r="8"/>
      <circle cx="118" cy="885" r="6"/>
      <circle cx="132" cy="900" r="9"/>
      <circle cx="108" cy="912" r="7"/>
      <circle cx="140" cy="950" r="11"/>
      <circle cx="168" cy="940" r="6"/>
    </g>
    <g fill="var(--paper)">
      <polygon points="82,186 85,193 92,193 86,197 88,204 82,200 76,204 78,197 72,193 79,193"/>
      <polygon points="105,196 107,201 112,201 108,204 110,209 105,206 100,209 102,204 98,201 103,201"/>
      <polygon points="876,1122 879,1129 886,1129 880,1133 882,1140 876,1136 870,1140 872,1133 866,1129 873,1129"/>
    </g>
  </svg>

  <svg class="compass-art" width="440" height="440" viewBox="0 0 440 440" role="img" aria-label="Compass rose over a vintage nautical chart with the party monogram">
    <defs>
      <radialGradient id="chartGlow" cx="50%" cy="50%" r="50%">
        <stop offset="0%" stop-color="#b58280"/>
        <stop offset="70%" stop-color="#6b3b3b"/>
        <stop offset="100%" stop-color="#000000"/>
      </radialGradient>
    </defs>
    <circle cx="241" cy="242" r="120" fill="url(#chartGlow)"/>
  </svg>

  <section class="details welcome">
    <p class="lead">WELCOME ABOARD!</p>
    <p class="lead">WE'LL HAVE LOTS OF FUN</p>
    <p class="sub">OUR LITTLE MARISOL IS TURNING ONE!</p>
  </section>

  <section class="details party">
    <p class="lead">YOU'RE INVITED TO A PARTY</p>
    <p class="sub">ON SATURDAY, AUGUST 7TH FROM 5 - 7 PM</p>
    <p class="venue">TIDE-AND-ROPE MIAMI</p>
  </section>

  <section class="details address">
    <p class="floor">THIRD FLOOR</p>
    <p class="line">4187 NORTH CORALWIND AVENUE</p>
    <p class="city">MIAMI, FL 33149-7812</p>
    <p class="note">PARKING TICKETS WILL BE VALIDATED</p>
  </section>

  <p class="footnote rsvp">PLEASE RSVP BY JULY 31ST TO MARISOLBIRTHDAY@BLUEFINMAIL.TEST OR 305-482-9067</p>
  <p class="footnote early">ARRIVE EARLY AT 4 PM TO JOIN US ON A SHORT PRE-PARTY BOAT TOUR OF THE MIAMI SKYLINE</p>
  <p class="footnote gifts">NO GIFTS PLEASE.&nbsp; A CONTRIBUTION TO TIDE AND ROPE'S PROGRAMS WOULD BE GREATLY APPRECIATED</p>

  <h2 class="headline headline--occasion">BIRTHDAY</h2>
</main>
</body>
</html>
```